Christmas social media advert post

I am looking for an eye catching advert for use mainly on social media posts.
The following is the detail of the event.

Christmas special offer-
£10pp,– offer includes –
Half an hour Toboggan track,
Half an hour Slingshot paintballs (20 paintballs pp) and safe target archery (under cover and indoor ranges). Activities all the family from age 4 to grandparents can join in,
Also available – Add on indoor activities including Mini Curling, Bead Blitz, Safe axe throwing, Air juggler – from £3.50pp and age 6plus
Café open for hot food and drinks in the ‘Fireside Frost Lodge and the heated Christmas marquee.

A basic idea I put together for what I feel is the important information is -

Christmas Special offer -
Starts Saturday 20th December.
£10pp – offer includes –
Half an hour Slingshot paintballs (20 paintballs pp) and safe target archery (under cover and indoor ranges). Activities all the family from age 4 to grandparents can join in. Booking is essential - details on how below.
Also available Add on indoor activities - including Mini Curling, Bead Blitz, Safe axe throwing, Air juggler – from £3.50pp and age 6plus.
Ages start from 4 plus.
All activities are great for children and adults so perfect for families as well as friends, parties and get togethers.
Free huge car parks,
Booking is easy-
Just Message from messenger (on this post) or email
martin@hollowbrookleisurepark.co.uk for availability of your preferred date and time.

I would be happy to send the detailed information to enquiries if it meant a better looking advert / post.

Full details are in the picture uploads, feel free to use as much or as little of the information as you feel best.

```html
<!DOCTYPE html>
<html lang="en">
<head>
<meta charset="utf-8">
<title>Christmas Special Offer</title>
<link href="https://fonts.googleapis.com/css2?family=Playfair+Display:wght@700&family=Didact+Gothic&family=Nunito+Sans:wght@800&display=swap" rel="stylesheet">
<style>
  :root {
    --cream: #f3e8d6;
    --panel: #f2e8d8;
    --panel-edge: #e6d6bd;
    --red: #c01f2f;
    --ink: #1e1a18;
    --pine: #1f5a45;
    --gold: #c99a4a;
    --berry: #b3121f;
    --photo-frame: #f4ead9;
  }
  * { margin: 0; padding: 0; box-sizing: border-box; }
  html, body { width: 1200px; height: 1200px; overflow: hidden; background: var(--cream); }
  .advert { position: relative; width: 1200px; height: 1200px; overflow: hidden; }

  .festive-frame {
    position: absolute; inset: 0;
    background:
      radial-gradient(ellipse 430px 420px at 600px 600px, #f7efe2 0%, #f1e2c8 55%, rgba(241,226,200,0) 80%),
      radial-gradient(circle at 1000px 140px, #c99a4a 0%, rgba(201,154,74,0) 22%),
      radial-gradient(circle at 80px 120px, #b3121f 0%, rgba(179,18,31,0) 18%),
      radial-gradient(circle at 1150px 1000px, #b3121f 0%, rgba(179,18,31,0) 14%),
      radial-gradient(circle at 600px 1160px, #1f5a45 0%, rgba(31,90,69,0) 30%),
      linear-gradient(135deg, #2b5d45 0%, #d9c39c 35%, #efdfc4 50%, #d9c39c 65%, #2b5d45 100%);
  }

  .photo {
    position: absolute; border-radius: 50%;
    border: 6px solid var(--photo-frame);
    box-shadow: 0 2px 8px rgba(0,0,0,0.25);
  }
  .photo--curling { left: 208px; top: -18px; width: 266px; height: 266px; background: linear-gradient(160deg, #e9d3ad, #c9a476); }
  .photo--axe { left: -6px; top: 497px; width: 206px; height: 206px; background: linear-gradient(140deg, #2c4f9c, #c8c2b6); }
  .photo--gel { left: 997px; top: 467px; width: 200px; height: 200px; background: linear-gradient(140deg, #4a4a52, #8c6b55); }
  .photo--archery { left: 118px; top: 957px; width: 240px; height: 240px; background: linear-gradient(160deg, #cdbb9e, #8f7a5f); }
  .photo--cabin { left: 927px; top: 977px; width: 246px; height: 246px; background: linear-gradient(160deg, #b88654, #e1c8a2); }

  .flourish {
    position: absolute; left: 500px; width: 200px; height: 36px;
    background: linear-gradient(90deg, rgba(31,90,69,0), rgba(31,90,69,0.55) 30%, rgba(192,31,47,0.6) 50%, rgba(31,90,69,0.55) 70%, rgba(31,90,69,0));
    border-radius: 18px; opacity: 0.7;
  }
  .flourish--top { top: 252px; }
  .flourish--bottom { top: 454px; }

  .headline {
    position: absolute; left: 0; width: 1200px; top: 292px; text-align: center;
    font-family: "Playfair Display", serif; font-weight: 700;
    font-size: 112px; line-height: 1; color: var(--red); letter-spacing: -1px;
  }
  .subhead {
    position: absolute; left: 0; width: 1200px; top: 398px; text-align: center;
    font-family: "Didact Gothic", sans-serif; font-size: 49px; line-height: 1;
    color: var(--ink); letter-spacing: 0.5px;
  }

  .offer { position: absolute; left: 270px; width: 659px; text-align: center; }
  .band {
    background: var(--red); color: #fff;
    font-family: "Nunito Sans", sans-serif; font-weight: 800;
    display: flex; align-items: center; justify-content: center;
  }
  .band--price { top: 528px; height: 44px; font-size: 30px; }
  .band--extras { top: 765px; height: 44px; font-size: 31px; }
  .box {
    background: var(--panel); border-bottom: 3px solid var(--panel-edge);
    font-family: "Didact Gothic", sans-serif; color: var(--ink);
    display: flex; flex-direction: column; justify-content: center;
  }
  .box--toboggan { top: 577px; height: 45px; font-size: 31px; }
  .box--slingshot { top: 628px; height: 131px; }
  .box--addons { top: 812px; height: 57px; font-size: 19.5px; line-height: 27px; }
  .box--cafe { top: 875px; height: 68px; font-size: 19.5px; line-height: 27px; }
  .lead { font-size: 31px; line-height: 36px; }
  .detail { font-size: 19.5px; line-height: 27px; }
  .accent { color: var(--red); font-family: "Nunito Sans", sans-serif; font-weight: 800; font-size: 0.95em; }
  .accent--soft { color: var(--red); }
  strong { font-weight: 700; font-family: "Nunito Sans", sans-serif; }
</style>
</head>
<body>
<main class="advert">
  <div class="festive-frame" role="img" aria-label="Border of pine branches, holly, red berries, gold and silver baubles, fairy lights and snow around a cream centre"></div>

  <div class="photo photo--curling" role="img" aria-label="Photo of a player sliding a mini curling stone on a wooden indoor lane"></div>
  <div class="photo photo--axe" role="img" aria-label="Photo of safe throwing axes stuck in a red, white and blue target"></div>
  <div class="photo photo--gel" role="img" aria-label="Photo of a player aiming a blaster in a neon-lit indoor range"></div>
  <div class="photo photo--archery" role="img" aria-label="Photo of an archer drawing a bow at targets in an undercover range"></div>
  <div class="photo photo--cabin" role="img" aria-label="Photo of a cosy wooden cabin café with a wood burner and hot chocolates"></div>

  <div class="flourish flourish--top" role="img" aria-label="Holly and scroll ornament"></div>
  <h1 class="headline">Christmas</h1>
  <p class="subhead">SPECIAL OFFER-</p>
  <div class="flourish flourish--bottom" role="img" aria-label="Holly and scroll ornament"></div>

  <div class="offer band band--price">£10pp,– OFFER INCLUDES</div>
  <div class="offer box box--toboggan">
    <p>Half an hour <span class="accent">Toboggan track,</span></p>
  </div>
  <div class="offer box box--slingshot">
    <p class="lead">Half an hour <span class="accent">Slingshot paintballs</span></p>
    <p class="detail">(20 paintballs pp) and safe target archery (under cover and<br>indoor ranges). Activities all the family from age 4 to<br>grandparents can join in,</p>
  </div>
  <div class="offer band band--extras">Also available</div>
  <div class="offer box box--addons">
    <p>Add on indoor activities including Mini Curling, Bead Blitz,<br>Safe axe throwing, Air juggler from <strong>£3.50pp</strong> and age 6plus</p>
  </div>
  <div class="offer box box--cafe">
    <p>Café open for hot food and drinks in the<br>‘<span class="accent--soft">Fireside Frost Lodge</span> and the heated Christmas marquee</p>
  </div>
</main>
</body>
</html>
```